Roadside building business signage for a holistic health clinic.

Replace signs as shown in the attached file. They are perforated stickers that go on the windows as shown. Looking for something that has our logo and says the name of the practice with logo (Fernbrook Health & Wellness) also boldly says Acupuncture, IV Vitamins, and Holistic Health.
Possibly our phone number as well 318-627-5194
Updates

Please don't use pink except the logo. Earthy, organic tone colors appreciated.

Need of eye catching window signage of a holistic clinic on a brick building. Pink, purple, sage green, white color. Logo is pink on a white background. Please don't overload with too much pink. Words to include are "Fernbrook Health and Wellness(name of business)", "Direct Primary Care", " Medical acupuncture", "IV Vitamin Therapy", "fernbrookcare-example.com","318-627-5194".

Target Market(s)

People will see in their cars passing by the building. Busy roadside so need to be visible while passing in fast speed.

Industry/Entity Type

Health & Wellness

Font styles to use
Sans Serif

Colors

Designer to choose colors to be used in the design.

Requirements
Must have
• On sign must have words Holistic Medicine, Medical Acupuncture, Direct Primary Care and IV vitamins.
Nice to have
• Simple, minimalistic, artistic yet has clear message. White, Black, Violet, Pink (logo), Dark green, Sage green.
Should not have
• Bold colors (red, yellow, blue), same tone colors. Blue waves on the current signage (uploaded file) must go.

```html
<!DOCTYPE html>
<html lang="en">
<head>
<meta charset="utf-8">
<title>Fernbrook Health &amp; Wellness — Window Signage</title>
<link rel="stylesheet" href="https://fonts.googleapis.com/css2?family=Encode+Sans+Semi+Condensed:wght@400;500&family=Jost:ital,wght@0,400;0,500;0,600;1,600&family=Marcellus&display=swap">
<style>
  :root {
    --backdrop: #000000;
    --cream: #f4ede1;
    --white: #ffffff;
    --sage: #4f7c62;
    --sage-text: #3f6f58;
    --forest: #264d3b;
    --mauve: #b2758e;
    --pattern: #d9d0d1;
    --pink: #e0508f;
    --olive: #5a5a1e;
  }
  * { box-sizing: border-box; margin: 0; padding: 0; }
  html, body { width: 716px; height: 1200px; overflow: hidden; background: var(--backdrop); }
  body { position: relative; font-family: "Jost", sans-serif; }

  .window-set { position: absolute; left: 29px; top: 405px; width: 657px; height: 390px; }
  .pane { position: absolute; width: 127px; height: 127px; background: var(--cream); overflow: hidden; }

  /* arch */
  .arch-half {
    position: absolute; top: 0; width: 127px; height: 127px; background: var(--cream);
    font-family: "Encode Sans Semi Condensed", sans-serif; font-weight: 400;
    color: var(--sage-text); font-size: 15px; line-height: 21.5px; padding-top: 33px;
  }
  .arch-left { left: 267.5px; border-top-left-radius: 100% 100%; text-align: right; padding-right: 9px; }
  .arch-right { left: 398.5px; border-top-right-radius: 100% 100%; text-align: left; padding-left: 8px; }

  /* brand panels */
  .brand-pane .wave { position: absolute; inset: 0; }
  .brand-name {
    position: absolute; left: 0; right: 0; top: 55px; text-align: center;
    font-family: "Marcellus", serif; font-size: 11px; letter-spacing: 2.2px; color: var(--sage-text);
  }
  .brand-sub {
    position: absolute; left: 0; right: 0; top: 69px; text-align: center;
    font-size: 3.6px; letter-spacing: 1.1px; color: var(--sage-text); text-transform: uppercase;
  }
  .brand-mark { position: absolute; left: 59px; top: 32px; width: 9px; height: 9px; border-radius: 50%; border: 1.2px solid var(--sage); }
  .mission {
    position: absolute; left: 13px; right: 13px; top: 85px; height: 32px;
    border-top: 0.6px solid var(--olive); border-bottom: 0.6px solid var(--olive);
    text-align: center; font-size: 4.6px; line-height: 9.5px; padding-top: 2.5px;
    color: var(--olive); text-transform: uppercase;
  }

  /* photo panels */
  .photo-pane { background: var(--white); }
  .photo-fill {
    position: absolute; inset: 0 0 10px 0;
    background: radial-gradient(circle at 50% 12%, #fbf6d8 0%, #a8b35a 22%, #6e7a3a 45%, #8d8b79 70%, #6e7478 100%);
  }
  .photo-frame { position: absolute; inset: 0; }

  /* info panels */
  .info-pane { text-align: center; }
  .info-title { margin-top: 11px; font-size: 8.2px; font-weight: 500; letter-spacing: 1.3px; color: var(--forest); }
  .benefits { list-style: none; margin-top: 3px; font-size: 4.8px; line-height: 7.5px; }
  .benefits li:nth-child(odd) { color: var(--forest); }
  .benefits li:nth-child(even) { color: var(--mauve); }
  .join { display: inline-block; margin-top: 9px; width: 45px; height: 9px; border: 0.6px solid var(--sage);
    font-size: 3.8px; line-height: 8px; font-weight: 600; color: var(--sage-text); text-transform: uppercase; }
  .info-phone { margin-top: 3px; font-size: 6px; letter-spacing: 0.5px; color: var(--forest); line-height: 7px; }
  .info-address { font-size: 5px; line-height: 6.5px; color: var(--forest); font-weight: 500; letter-spacing: 0.2px; }
  .info-web { margin-top: 2px; font-size: 5.3px; letter-spacing: 0.5px; color: var(--mauve); }

  /* name panels */
  .name-pane { background: var(--white); text-align: center; }
  .name-pane .base { position: absolute; inset: 0; }
  .name-dot { position: absolute; left: 50.5px; top: 11px; width: 26px; height: 26px; border-radius: 50%; background: var(--pink); }
  .name-title { position: absolute; left: 0; right: 0; top: 54px; font-family: "Marcellus", serif;
    font-size: 15px; letter-spacing: 1.6px; color: var(--sage-text); }
  .name-sub { position: absolute; left: 0; right: 0; top: 75px; font-size: 5.6px; letter-spacing: 2px; color: var(--sage-text); }
  .name-services { position: absolute; left: 0; right: 0; top: 99px; font-size: 4.8px; font-style: italic; font-weight: 600; color: var(--sage-text); }
  .name-phone { position: absolute; left: 0; right: 0; top: 106px; font-size: 6px; letter-spacing: 0.5px; color: var(--forest); }
  .name-web { position: absolute; left: 0; right: 0; top: 114px; font-size: 5.3px; letter-spacing: 0.6px; color: var(--mauve); }

  /* emblem panel */
  .emblem-dot { position: absolute; left: 47px; top: 44px; width: 32px; height: 32px; border-radius: 50%; background: var(--pink); }
  .emblem-name { position: absolute; left: 0; right: 0; top: 83px; text-align: center; font-family: "Marcellus", serif; font-size: 10px; letter-spacing: 1.5px; color: var(--sage-text); }
</style>
</head>
<body>
<main class="window-set">

  <div class="arch-half arch-left">DIRECT<br>HOLISTIC<br>PRIMARY<br>CARE</div>
  <div class="arch-half arch-right">DIRECT<br>HOLISTIC<br>PRIMARY<br>CARE</div>

  <!-- upper row -->
  <section class="pane brand-pane" style="left:136px;top:131px;">
    <svg class="wave" viewBox="0 0 127 127">
      <path d="M0 0 H14 C20 20 30 28 40 30 C50 32 56 36 63.5 42 C71 36 77 32 87 30 C97 28 107 20 113 0 H127 V28 C115 28 108 40 100 50 H27 C19 40 12 28 0 28 Z" fill="var(--pattern)" role="img" aria-label="Soft textured pattern"/>
      <path d="M14 0 H113 C107 20 97 28 87 30 C77 32 71 36 63.5 42 C56 36 50 32 40 30 C30 28 20 20 14 0 Z" fill="var(--sage)"/>
    </svg>
    <span class="brand-mark"></span>
    <div class="brand-name">FERNBROOK</div>
    <div class="brand-sub">Health &amp; Wellness</div>
    <p class="mission">A direct primary care practice<br>focused on a more holistic<br>and personal approach to medicine.</p>
  </section>

  <section class="pane photo-pane" style="left:267.5px;top:131px;">
    <div class="photo-fill" role="img" aria-label="Photo of a large old tree with spreading roots and sunlight through leaves"></div>
    <svg class="photo-frame" viewBox="0 0 127 127">
      <path d="M0 55 C6 70 10 90 22 100 C32 108 40 110 46 118 C52 124 58 124 63.5 122 C69 124 75 124 81 118 C87 110 95 108 105 100 C117 90 121 70 127 55 V127 H0 Z" fill="var(--pattern)"/>
      <path d="M0 110 C20 106 36 116 56 114 C78 112 92 104 127 110 V127 H0 Z" fill="var(--white)"/>
      <path d="M0 114 C22 110 38 120 60 118 C82 116 96 108 127 114" fill="none" stroke="var(--pattern)" stroke-width="0.8"/>
    </svg>
  </section>

  <section class="pane photo-pane" style="left:398.5px;top:131px;">
    <div class="photo-fill" role="img" aria-label="Photo of a large old tree with spreading roots and sunlight through leaves"></div>
    <svg class="photo-frame" viewBox="0 0 127 127">
      <path d="M0 55 C6 70 10 90 22 100 C32 108 40 110 46 118 C52 124 58 124 63.5 122 C69 124 75 124 81 118 C87 110 95 108 105 100 C117 90 121 70 127 55 V127 H0 Z" fill="var(--pattern)"/>
      <path d="M0 110 C20 106 36 116 56 114 C78 112 92 104 127 110 V127 H0 Z" fill="var(--white)"/>
      <path d="M0 114 C22 110 38 120 60 118 C82 116 96 108 127 114" fill="none" stroke="var(--pattern)" stroke-width="0.8"/>
    </svg>
  </section>

  <section class="pane brand-pane" style="left:529.5px;top:131px;">
    <svg class="wave" viewBox="0 0 127 127">
      <path d="M0 0 H14 C20 20 30 28 40 30 C50 32 56 36 63.5 42 C71 36 77 32 87 30 C97 28 107 20 113 0 H127 V28 C115 28 108 40 100 50 H27 C19 40 12 28 0 28 Z" fill="var(--pattern)" role="img" aria-label="Soft textured pattern"/>
      <path d="M14 0 H113 C107 20 97 28 87 30 C77 32 71 36 63.5 42 C56 36 50 32 40 30 C30 28 20 20 14 0 Z" fill="var(--sage)"/>
    </svg>
    <span class="brand-mark"></span>
    <div class="brand-name">FERNBROOK</div>
    <div class="brand-sub">Health &amp; Wellness</div>
    <p class="mission">A direct primary care practice<br>focused on a more holistic<br>and personal approach to medicine.</p>
  </section>

  <!-- lower row -->
  <section class="pane emblem-pane" style="left:0;top:263px;">
    <span class="emblem-dot"></span>
    <div class="emblem-name">FERNBROOK</div>
  </section>

  <section class="pane info-pane" style="left:136px;top:263px;">
    <h2 class="info-title">DIRECT PRIMARY CARE</h2>
    <ul class="benefits">
      <li>30-90 Minutes Relaxed Appointment</li>
      <li>Price Transparency no Copays</li>
      <li>Minimal Wait Times</li>
      <li>Direct communication with your Physician</li>
      <li>Easy to Book Appointment</li>
    </ul>
    <div class="join">Join us today!</div>
    <p class="info-phone">318-627-5194</p>
    <p class="info-address">1420 Willow Bend Rd., STE 2B<br>Alderton, IN 46990</p>
    <p class="info-web">fernbrookcare-example.com</p>
  </section>

  <section class="pane name-pane" style="left:267.5px;top:263px;">
    <svg class="base" viewBox="0 0 127 127"><path d="M0 96 C40 88 90 86 127 90 V127 H0 Z" fill="var(--cream)"/><path d="M0 94 C40 86 90 84 127 88" fill="none" stroke="var(--sage)" stroke-width="0.8"/></svg>
    <span class="name-dot"></span>
    <div class="name-title">FERNBROOK</div>
    <div class="name-sub">HEALTH &amp; WELLNESS</div>
    <div class="name-services">Acupuncture, IV Vitamins, and Holistic Health.</div>
    <div class="name-phone">318-627-5194</div>
    <div class="name-web">fernbrookcare-example.com</div>
  </section>

  <section class="pane name-pane" style="left:398.5px;top:263px;">
    <svg class="base" viewBox="0 0 127 127"><path d="M0 96 C40 88 90 86 127 90 V127 H0 Z" fill="var(--cream)"/><path d="M0 94 C40 86 90 84 127 88" fill="none" stroke="var(--sage)" stroke-width="0.8"/></svg>
    <span class="name-dot"></span>
    <div class="name-title">FERNBROOK</div>
    <div class="name-sub">HEALTH &amp; WELLNESS</div>
    <div class="name-services">Acupuncture, IV Vitamins, and Holistic Health.</div>
    <div class="name-phone">318-627-5194</div>
    <div class="name-web">fernbrookcare-example.com</div>
  </section>

  <section class="pane info-pane" style="left:529.5px;top:263px;">
    <h2 class="info-title">DIRECT PRIMARY CARE</h2>
    <ul class="benefits">
      <li>30-90 Minutes Relaxed Appointment</li>
      <li>Price Transparency no Copays</li>
      <li>Minimal Wait Times</li>
      <li>Direct communication with your Physician</li>
      <li>Easy to Book Appointment</li>
    </ul>
    <div class="join">Join us today!</div>
    <p class="info-phone">318-627-5194</p>
    <p class="info-address">1420 Willow Bend Rd., STE 2B<br>Alderton, IN 46990</p>
    <p class="info-web">fernbrookcare-example.com</p>
  </section>

</main>
</body>
</html>
```